missions focus sunday

i am a christian who is tasked to do a simple presentation of missions work in northern germany. i have some ideas which i have sketched out as enclosed.
can you do the postcard in black background with words/diagrams in white? thanks

Industry/Entity Type

Christian

```html
<!DOCTYPE html>
<html lang="en">
<head>
<meta charset="utf-8">
<title>Missions Focus Sunday</title>
<link rel="stylesheet" href="https://fonts.googleapis.com/css2?family=Source+Sans+3:ital,wght@1,700&display=swap">
<style>
  :root {
    --ink: #000000;
    --paper: #ffffff;
    --mark: #d9d9d9;
  }
  * { margin: 0; padding: 0; box-sizing: border-box; }
  html, body {
    width: 1200px;
    height: 800px;
    overflow: hidden;
    background: var(--ink);
  }
  .postcard {
    position: relative;
    width: 1200px;
    height: 800px;
    background: var(--ink);
    font-family: "Source Sans 3", "Myriad Pro", sans-serif;
    font-weight: 700;
    font-style: italic;
  }
  .cycle-diagram {
    position: absolute;
    inset: 0;
    width: 1200px;
    height: 800px;
  }
  .arrow-band { fill: var(--paper); }
  .arrow-rule { fill: none; stroke: var(--paper); stroke-width: 3; stroke-linecap: round; }
  .step-box { fill: var(--paper); }
  .cloud-halo { fill: none; stroke: var(--paper); stroke-width: 22; stroke-linejoin: round; }
  .cloud-gap { fill: none; stroke: var(--ink); stroke-width: 10; stroke-linejoin: round; }
  .cloud-body { fill: var(--paper); }

  .footsteps-icon {
    position: absolute;
    left: 288px;
    top: 45px;
    width: 114px;
    height: 148px;
    border-radius: 40px;
    background: radial-gradient(ellipse at center, var(--mark) 0%, #6a6a6a 60%, var(--ink) 100%);
  }
  .caption {
    position: absolute;
    color: var(--paper);
    font-size: 36px;
    line-height: 1.0;
    text-align: center;
  }
  .caption--power { left: 108px; top: 290px; width: 130px; }
  .caption--call { left: 870px; top: 562px; width: 190px; text-align: right; }
  .cloud-label {
    position: absolute;
    left: 466px;
    top: 384px;
    width: 290px;
    color: var(--ink);
    font-size: 34px;
    line-height: 1.05;
    text-align: center;
  }
</style>
</head>
<body>
<main class="postcard">
  <svg class="cycle-diagram" viewBox="0 0 1000 667" aria-hidden="true">
    <!-- upper arrow: rises on the left, points right -->
    <path class="arrow-band" d="M258 478 Q238 172 556 140 L556 124 L608 165 L556 202 L556 180 Q292 190 262 478 Z"/>
    <path class="arrow-rule" d="M263 462 Q296 200 552 190"/>
    <!-- lower arrow: falls on the right, points left -->
    <path class="arrow-band" d="M738 232 Q772 560 440 560 L440 580 L389 544 L440 507 L440 525 Q732 524 738 232 Z"/>
    <path class="arrow-rule" d="M728 244 Q734 506 446 514"/>
    <!-- step boxes -->
    <rect class="step-box" x="632" y="128" width="135" height="75"/>
    <rect class="step-box" x="217" y="503" width="134" height="75"/>
    <!-- centre cloud -->
    <g class="cloud">
      <path class="cloud-halo" d="M370 430 A45 45 0 0 1 345 350 A55 55 0 0 1 420 290 A75 75 0 0 1 540 255 A65 65 0 0 1 630 310 A50 50 0 0 1 650 400 A40 40 0 0 1 600 435 A60 60 0 0 1 500 440 A60 60 0 0 1 400 438 A40 40 0 0 1 370 430 Z"/>
      <path class="cloud-gap" d="M370 430 A45 45 0 0 1 345 350 A55 55 0 0 1 420 290 A75 75 0 0 1 540 255 A65 65 0 0 1 630 310 A50 50 0 0 1 650 400 A40 40 0 0 1 600 435 A60 60 0 0 1 500 440 A60 60 0 0 1 400 438 A40 40 0 0 1 370 430 Z"/>
      <path class="cloud-body" d="M370 430 A45 45 0 0 1 345 350 A55 55 0 0 1 420 290 A75 75 0 0 1 540 255 A65 65 0 0 1 630 310 A50 50 0 0 1 650 400 A40 40 0 0 1 600 435 A60 60 0 0 1 500 440 A60 60 0 0 1 400 438 A40 40 0 0 1 370 430 Z"/>
    </g>
  </svg>

  <div class="footsteps-icon" role="img" aria-label="Pair of white footprints walking upward"></div>

  <p class="caption caption--power">The<br>Power<br>of 2</p>
  <p class="cloud-label">Last Night<br>Dream of this</p>
  <p class="caption caption--call">Wiweiy<br>the “wme”<br>call</p>
</main>
</body>
</html>
```